Business Card Design for a Jockey's Agent

A business card design that helps to develop a brand or identity for myself, the agent, perhaps on one side with a clean minimalist design, and on the other side a simple design with the two jockeys names i currently represent. Those jockeys may change twice a year as they move around the country, switch agents, etc, so i think keeping one side designed to promote the agent and a second side that can be changed easily to identify the jockeys i currently represent would be the best.

Target Market(s)

Thoroughbred racehorse trainers

Industry/Entity Type

Business

Contact Information for Business Card

Garrett Lindqvist - Jockey Agent
mobile (614) 382 7291
garrettplindqvist7mailhub.example

Jockeys: Everett Kline, Tobias Renwick

Font styles to use
Serif

Requirements
Must have
• contact info and modern feel and font
Nice to have
• clean minimalist element of racing, jockey silk, helmut or crop, finish marker pole from racetrack etc,
Should not have
• DONT HAVE ANY KIND OF LOGO ETC. IMAGE IS ONE OF MY RACEHORSES TO HELP FINISH BRIEF.
• racing horse, stuffy vintage racing feel or Weekly Paddock Sheet fonts

```html
<!DOCTYPE html>
<html lang="en">
<head>
<meta charset="utf-8">
<title>Garrett Lindqvist – Jockey Agent Business Card</title>
<link rel="stylesheet" href="https://fonts.googleapis.com/css2?family=Cinzel:wght@400;600&family=Libre+Baskerville&family=Open+Sans:wght@400;600&display=swap">
<style>
  :root {
    --royal: #1f3f9e;
    --royal-deep: #18348a;
    --royal-light: #2f55b8;
    --silhouette: #4a6cc4;
    --paper: #ffffff;
    --paper-shade: #eef0f4;
    --ink: #1d3a95;
    --backdrop: #e7e4df;
  }
  * { box-sizing: border-box; margin: 0; padding: 0; }
  html, body { width: 1200px; height: 912px; overflow: hidden; }
  body { background: var(--backdrop); position: relative; font-family: "Open Sans", sans-serif; }

  .card { position: absolute; width: 520px; height: 313px; top: 300px; box-shadow: 0 6px 18px rgba(0,0,0,.18); overflow: hidden; }

  /* Reverse side: brand feature artwork */
  .card--back { left: 50px; background: radial-gradient(ellipse at 35% 40%, var(--royal-light), var(--royal) 55%, var(--royal-deep)); }
  .card--back .feature-art { position: absolute; left: 77px; top: 86px; width: 374px; height: 227px;
    background: linear-gradient(100deg, rgba(110,140,215,.55), rgba(95,125,205,.45) 60%, rgba(80,110,195,.3));
    border-radius: 120px 170px 0 0; }

  /* Front side */
  .card--front { left: 630px; background: linear-gradient(180deg, var(--paper) 40%, var(--paper-shade)); }
  .header-band { position: absolute; left: 0; top: 0; width: 100%; height: 105px;
    background: linear-gradient(90deg, var(--royal-deep), var(--royal) 60%, var(--royal-light)); }
  .header-rule { position: absolute; left: 0; top: 109px; width: 100%; height: 4px; background: var(--royal); }
  .header-art { position: absolute; left: 6px; top: 23px; width: 161px; height: 82px;
    background: linear-gradient(90deg, rgba(255,255,255,.92), rgba(255,255,255,.7));
    border-radius: 50px 80px 0 0; }

  .agent-name { position: absolute; left: 142px; top: 12px; width: 266px; text-align: center; }
  .agent-name .line { height: 1.5px; background: var(--paper); }
  .agent-name h1 { font-family: "Cinzel", serif; font-weight: 400; font-size: 23px; color: var(--paper); letter-spacing: .5px; padding: 3px 0 2px; white-space: nowrap; }
  .agent-role { position: absolute; left: 142px; top: 56px; width: 266px; text-align: center;
    font-size: 16px; color: var(--paper); }

  .roster { position: absolute; left: 21px; top: 168px; color: var(--ink); }
  .roster h2 { font-weight: 400; font-size: 17px; }
  .roster ul { list-style: none; margin: 11px 0 0 34px; font-family: "Libre Baskerville", serif; font-size: 19px; line-height: 27px; }

  .divider { position: absolute; left: 264px; top: 140px; width: 2px; height: 150px;
    background: linear-gradient(180deg, transparent, var(--ink) 30%, var(--ink) 70%, transparent); }

  .contact { position: absolute; left: 312px; top: 178px; list-style: none; color: var(--ink); font-size: 10px; }
  .contact li { display: flex; align-items: center; gap: 6px; height: 20px; white-space: nowrap; }
  .contact svg { width: 13px; height: 13px; flex: none; }
  .contact .dot { width: 11px; height: 11px; border-radius: 50%; background: var(--ink); flex: none; margin-right: 2px; }
</style>
</head>
<body>
  <section class="card card--back">
    <div class="feature-art" role="img" aria-label="Large faint silhouette of a racehorse and jockey in lighter blue"></div>
  </section>

  <section class="card card--front">
    <div class="header-band"></div>
    <div class="header-rule"></div>
    <div class="header-art" role="img" aria-label="White silhouette of a racehorse and jockey"></div>
    <div class="agent-name">
      <div class="line"></div>
      <h1>Garrett Lindqvist</h1>
      <div class="line"></div>
    </div>
    <p class="agent-role">Jockey Agent</p>

    <div class="roster">
      <h2>Jockeys:</h2>
      <ul>
        <li>Everett Kline</li>
        <li>Tobias Renwick</li>
      </ul>
    </div>

    <div class="divider"></div>

    <ul class="contact">
      <li>
        <svg viewBox="0 0 16 16" aria-hidden="true"><circle cx="8" cy="8" r="7" fill="none" stroke="currentColor" stroke-width="1.4"/><path d="M5.5 4.5l1.5 1.5-1 1c.5 1.2 1.4 2.1 2.6 2.6l1-1 1.5 1.5-1 1.2C7.6 11 5 8.4 4.5 5.9z" fill="currentColor"/></svg>
        (614) 382 7291
      </li>
      <li>
        <svg viewBox="0 0 16 16" aria-hidden="true"><rect x="1.5" y="3.5" width="13" height="9" fill="currentColor"/><path d="M1.5 3.5L8 9l6.5-5.5" fill="none" stroke="#fff" stroke-width="1.2"/></svg>
        garrettplindqvist7mailhub.example
      </li>
      <li><span class="dot"></span>garrettlindqvist</li>
      <li><span class="dot"></span>@garrettlindqvist</li>
    </ul>
  </section>
</body>
</html>
```